New Plumbing Company

We are looking for a smart and creative business card design for our new plumbing company. We are looking for creativity and originality in our business cards.

Industry/Entity Type

Plumbing

Contact Information for Business Card

Crestline Plumbing
Peter Halvane
Managing Director
Telephone Number : 0481529604
Email : service@crestlineplumbing.com.au
Website : www.crestlineplumbing.com.au
Lic. 508264K

Colors
0692cd
33a6d7
000000

Requirements
Must have
• I want the business card to be designed on a black background using the blue tones i have selected as seen in the company logo.

```html
<!DOCTYPE html>
<html lang="en">
<head>
<meta charset="utf-8">
<title>Crestline Plumbing – Business Card</title>
<link rel="stylesheet" href="https://fonts.googleapis.com/css2?family=Roboto:wght@300;400&display=swap">
<style>
  :root {
    --blue-deep: #0692cd;
    --blue-light: #33a6d7;
    --blue-shade: #1570a8;
    --band-black: #232225;
    --card-white: #f4f4f4;
    --card-grey: #e2e2e2;
    --ink: #2b2b2b;
    --page: #e7e4df;
  }
  * { margin: 0; padding: 0; box-sizing: border-box; }
  html, body {
    width: 1200px; height: 600px; overflow: hidden;
    background: var(--page);
    font-family: "Roboto", Arial, sans-serif;
  }
  .sheet {
    width: 1200px; height: 600px;
    display: flex; align-items: center; justify-content: space-evenly;
  }
  .card {
    width: 500px; height: 286px; position: relative; overflow: hidden;
    box-shadow: 0 10px 28px rgba(0,0,0,.22);
  }

  /* Front */
  .card-front {
    background: linear-gradient(160deg, #ffffff 0%, var(--card-white) 55%, var(--card-grey) 100%);
  }
  .brand {
    position: absolute; left: 30px; top: 50%; transform: translateY(-50%);
    width: 228px;
    display: flex; align-items: center; gap: 10px;
  }
  .brand-dot {
    width: 26px; height: 26px; border-radius: 50%; flex: none;
    border: 2px solid var(--blue-deep);
  }
  .brand-name {
    font-weight: 300; font-size: 22px; color: var(--blue-deep);
    white-space: nowrap;
  }
  .divider {
    position: absolute; left: 272px; top: 36px; bottom: 36px; width: 1px;
    background: linear-gradient(to bottom, transparent, #bdbdbd 25%, #bdbdbd 75%, transparent);
  }
  .details {
    position: absolute; left: 292px; top: 44px; right: 12px;
    color: var(--ink); font-weight: 300;
  }
  .person-name { font-size: 17px; font-weight: 400; }
  .person-title { font-size: 12px; color: var(--blue-deep); margin-top: 3px; }
  .address { font-size: 11.5px; line-height: 1.45; margin-top: 20px; }
  .contacts { list-style: none; margin-top: 18px; font-size: 11.5px; }
  .contacts li {
    display: flex; align-items: center; gap: 8px;
    margin-bottom: 5px; line-height: 14px; white-space: nowrap;
  }
  .contacts svg { display: block; width: 11px; height: 11px; flex: none; }

  /* Back */
  .card-back {
    background: linear-gradient(100deg, var(--blue-shade) 0%, var(--blue-deep) 45%, var(--blue-light) 100%);
  }
  .band {
    position: absolute; left: 0; right: 0; top: 92px; height: 96px;
    background: var(--band-black);
    display: flex; flex-direction: column; justify-content: center; align-items: center;
    color: #fff; font-size: 14px; line-height: 1.35; text-align: center;
  }
  .licence {
    position: absolute; left: 30px; right: 30px; bottom: 30px;
    display: flex; align-items: center; gap: 14px;
    color: rgba(255,255,255,.85); font-size: 11px; letter-spacing: 4px;
  }
  .licence::before, .licence::after {
    content: ""; flex: 1; height: 1px; background: rgba(255,255,255,.5);
  }
</style>
</head>
<body>
<main class="sheet">
  <section class="card card-front" aria-label="Card front">
    <div class="brand">
      <span class="brand-dot"></span>
      <span class="brand-name">Crestline Plumbing</span>
    </div>
    <div class="divider"></div>
    <div class="details">
      <p class="person-name">Peter Halvane</p>
      <p class="person-title">Managing Director</p>
      <p class="address">Here your company or<br>home address</p>
      <ul class="contacts">
        <li>
          <svg viewBox="0 0 12 12" aria-hidden="true"><path fill="#0692cd" d="M3 1.2h1.8l.9 2.4-1.1.8a6 6 0 0 0 3 3l.8-1.1 2.4.9V9a1.3 1.3 0 0 1-1.3 1.3A8 8 0 0 1 1.7 2.5 1.3 1.3 0 0 1 3 1.2z"/></svg>
          <span>0481529604</span>
        </li>
        <li>
          <svg viewBox="0 0 12 12" aria-hidden="true"><rect x="0.5" y="2" width="11" height="8" rx="1" fill="#0692cd"/><path d="M1 2.8 6 6.6l5-3.8" fill="none" stroke="#fff" stroke-width="1"/></svg>
          <span>service@crestlineplumbing.com.au</span>
        </li>
        <li>
          <svg viewBox="0 0 12 12" aria-hidden="true"><circle cx="6" cy="6" r="5.5" fill="#0692cd"/><path d="M.8 6h10.4M6 .5c-2.4 2.8-2.4 8.2 0 11M6 .5c2.4 2.8 2.4 8.2 0 11" fill="none" stroke="#fff" stroke-width=".8"/></svg>
          <span>www.crestlineplumbing.com.au</span>
        </li>
      </ul>
    </div>
  </section>

  <section class="card card-back" aria-label="Card back">
    <div class="band">
      <p>Plumbing Draining Gas Fitting</p>
      <p>24/7 Emergency Service</p>
    </div>
    <p class="licence">Lic.508264K</p>
  </section>
</main>
</body>
</html>
```